2-Page Flyer for the Information Session about the Tranquil Venture Course

This is a flyer to announce/advertise an evening Information Session about the Tranquil Venture Course. This Program aims at mindfully rethinking and redesigning work (and life) for people who feel stuck or not entirely satisfied with their work and/or life (please see draft flyer attached for more details). This Program is property of Brightfold Joy, a company that uses a combination of Mindfulness, Design, and Entrepreneurship to help people achieve greater happiness (in their work and lives).
Updates

Target Market(s)

People who feel stuck or not entirely satisfied with their work and/or life (please see draft flyer attached for more details)

Font styles to use
Serif
Sans Serif

Colors
ffffff
f37122
33a6d7
acd037

Requirements
Must have
• All of what I will say below is suggestive (I’m not a design expert), and I’m open to divert from it, if it makes sense and feels more interesting.
• I thought initially of a 2-page flyer (please see draft flyer attached). The first page could help people grasp the essence of the event quickly (in 1 or 2 minutes), and then, if they are interested/motivated, they would continue reading through page 2, which has more info about the Program in itself.
• Potential Structure
• Page 1
• . About the Information Session on the Tranquil Venture Course
• . Visible Date & Time, Contacts, Venue (and other relevant info)
• . About me (the facilitator)
• Page 2
• . About the Tranquil Venture Course
• I include a Powerpoint draft of the flyer with the content. The design is rudimentary and precarious from an aesthetics/organization point of view, and this is mainly where I need help (and maybe in other aspects too!).
• On the flyer, I would like to include:
• . A photo of myself (I attach 1 picture).
• . 1 or 2 beautiful-nature photos (cropped or full). One may have to do with looking at the sky, dreaming, and imagining a new work and life (2 photos with sky and clouds attached). The other has to do with walking the transformation journey (the photo with the person walking through the forest path).
• . brightfold joy logo or logos (there are two slightly different ones, that can be used for different purposes). For the first page, I would like the brightfold joy logo that has "brightfold joy" written on the bottom, with the saying "Stillness, Craft and Venture for Joy" beneath. This is the main logo. For the 2nd page, you can choose the logo that adapts better.
• - Where it says the "the way out is in" it would be great to have a similar font to the one I attach (see file "Font_the_way_out_is_in.png" and Ankecallig-fg.ttf
Nice to have
• In terms of colours, I would not divert much from the logo colours (and of course white and black). I would like the flyer to be quite white. Almost like fairy-tale white: the white horse, the white snow, the white of the stars, the white heaven. White could be the base colour. White means peace, tranquillity, calm contentment, a smile.
• And then use the other colours. The green of the mindfulness. The blue of the sky, the dreams. And the orange of the sun, the energy, the fire, the action. And maybe the black for text.
• Where it says the "the way out is in" it would be great to have a similar font to the one I attach (see file "Font_the_way_out_is_in".
• I would like this flyer to be a piece of art, in every possible way. Simple, beautiful, ease, light, peaceful, calm happy. Just like the Tranquil Venture Course and brightfold joy Company that I am creating intends to be. The mission of this Program and Company is to be a designer, a painter (a Picasso) of happier and more fulfilling human lives.
• I am very much looking forward to seeing your proposal(s).

```html
<!DOCTYPE html>
<html lang="en">
<head>
<meta charset="utf-8">
<title>Tranquil Venture Course – Free Information Session</title>
<link rel="stylesheet" href="https://fonts.googleapis.com/css2?family=Bowlby+One&family=Montserrat:ital,wght@0,400;0,600;0,700;1,700&display=swap">
<style>
  :root {
    --white: #ffffff;
    --orange: #f37122;
    --blue: #33a6d7;
    --green: #acd037;
    --ink: #3a3a3a;
    --ink-soft: #6b6b6b;
    --page-bg: #f2f2f2;
    --rule: #d9d9d9;
  }
  * { box-sizing: border-box; margin: 0; padding: 0; }
  html, body { width: 1200px; height: 574px; overflow: hidden; background: var(--page-bg); }
  body { font-family: "Montserrat", sans-serif; color: var(--ink); position: relative; }

  .flyer {
    position: absolute; left: 409px; top: 17px;
    width: 382px; height: 540px;
    background: var(--white); border: 1px solid #222;
    overflow: hidden;
  }
  .brand { position: absolute; top: 22px; left: 0; width: 100%; text-align: center; }
  .brand-mark { width: 26px; height: 26px; border-radius: 50%; background: var(--orange); margin: 0 auto 8px; }
  .brand-name { font-size: 13px; font-weight: 400; color: var(--blue); letter-spacing: -0.2px; }
  .brand-tagline { font-size: 3.6px; font-weight: 600; text-transform: uppercase; color: var(--ink); margin-top: 2px; letter-spacing: 0.1px; }

  .title {
    position: absolute; top: 82px; left: 0; width: 100%; text-align: center;
    font-family: "Bowlby One", sans-serif; color: var(--orange);
    -webkit-text-stroke: 1px var(--blue); line-height: 1.05;
  }
  .title-line-1 { font-size: 30px; display: block; }
  .title-line-2 { font-size: 24px; display: block; margin-top: 2px; }
  .title-line-3 { font-size: 21px; display: block; margin-top: 2px; }

  .session-box {
    position: absolute; top: 187px; left: 81px; width: 219px; height: 52px;
    text-align: center;
  }
  .session-box svg { position: absolute; inset: 0; }
  .session-heading { position: relative; font-size: 11.5px; font-weight: 400; color: var(--ink); margin-top: 8px; letter-spacing: 0.2px; }
  .session-details { position: relative; font-size: 6.6px; color: var(--ink-soft); line-height: 1.8; margin-top: 1px; }

  .intro, .audience {
    position: absolute; top: 257px; font-size: 6.6px; line-height: 1.4; color: var(--ink-soft);
  }
  .intro { left: 47px; width: 135px; }
  .audience { left: 199px; width: 150px; }
  .audience h2 { font-size: 7.4px; font-weight: 700; color: var(--ink); margin-bottom: 1px; }

  .facilitator-photo {
    position: absolute; top: 345px; left: 38px; width: 74px; height: 94px;
    background: linear-gradient(160deg, #e4e1e6 0%, #c9c6cc 45%, #3d4a5a 100%);
    border-top: 2px solid var(--green); border-right: 2px solid var(--orange);
    border-left: 2px solid var(--blue); border-bottom: 2px solid var(--blue);
  }
  .facilitator-name { position: absolute; top: 443px; left: 38px; font-size: 7.4px; font-weight: 700; font-style: italic; color: var(--ink-soft); }
  .facilitator-role { position: absolute; top: 453px; left: 38px; font-size: 5px; line-height: 1.35; color: var(--ink-soft); }

  .bio { position: absolute; top: 346px; left: 120px; width: 232px; font-size: 6.2px; line-height: 10.9px; color: var(--ink-soft); }
  .more-link { position: absolute; top: 478px; left: 119px; font-size: 7.2px; font-weight: 700; color: #111; }

  .footer-rule { position: absolute; top: 497px; left: 0; width: 100%; height: 2px; background: var(--rule); }
  .contact { position: absolute; display: flex; align-items: center; gap: 4px; font-size: 6.2px; color: var(--ink); }
  .contact-email { top: 509px; left: 38px; }
  .contact-divider { position: absolute; top: 506px; left: 158px; width: 1px; height: 13px; background: #999; }
  .contact-label { position: absolute; top: 506px; left: 190px; font-size: 6.2px; font-weight: 700; text-align: right; line-height: 1.3; }
  .contact-phone { top: 509px; left: 236px; }
  .dot-icon { width: 8px; height: 8px; border-radius: 50%; display: inline-block; }

  .colour-bar { position: absolute; bottom: 0; left: 0; width: 100%; height: 8px; display: flex; }
  .colour-bar span:nth-child(1) { width: 283px; background: var(--blue); }
  .colour-bar span:nth-child(2) { width: 66px; background: var(--green); }
  .colour-bar span:nth-child(3) { flex: 1; background: var(--orange); }
</style>
</head>
<body>
<main class="flyer">
  <header class="brand">
    <div class="brand-mark"></div>
    <div class="brand-name">brightfold joy</div>
    <div class="brand-tagline">Stillness, Craft and Venture for Joy</div>
  </header>

  <h1 class="title">
    <span class="title-line-1">TRANQUIL</span>
    <span class="title-line-2">VENTURE</span>
    <span class="title-line-3">COURSE</span>
  </h1>

  <section class="session-box">
    <svg width="219" height="52" viewBox="0 0 219 52" aria-hidden="true">
      <line x1="16" y1="0.5" x2="203" y2="0.5" stroke="#acd037" stroke-width="1"/>
      <polyline points="16,4 1,4 1,48 16,48" fill="none" stroke="#33a6d7" stroke-width="1.4"/>
      <polyline points="203,4 218,4 218,48 203,48" fill="none" stroke="#33a6d7" stroke-width="1.4"/>
    </svg>
    <h2 class="session-heading">FREE INFORMATION SESSION</h2>
    <p class="session-details">Date : Thursday 5th September 2019 &nbsp;|&nbsp; Time : 19:30 to 21:00<br>Venue: Lumen Coworking, C/ Olmera 42, Barcelona</p>
  </section>

  <p class="intro">The purpose of this free Information Session is to give you a real insight into the Tranquil Venture Course and how it can help you make the most of your professional and personal life.</p>

  <div class="audience">
    <h2>WHO CAN COME</h2>
    <p>Whether you come on your own, or with friends or family, you'll be warmly welcomed. The session will take place on Thursday the 5th September 2019, from 19:30 to 21:00, at LUMEN Coworking. Please see information below to get in contact or to book a seat.</p>
  </div>

  <div class="facilitator-photo" role="img" aria-label="Portrait photo of the facilitator, Dr Marco Vella"></div>
  <p class="facilitator-name">Dr Marco Vella</p>
  <p class="facilitator-role">Visiting Research Fellow<br>Northvale University</p>

  <p class="bio">Marco joined the Northvale University School of Management as a Lecturer in Entrepreneurship in 2015. He completed his PhD in Entrepreneurship at Kelmoor Business School in 2014, receiving the prestigious Institute of Enterprise Studies' Rowan Doctoral Award. He began his business career as a Production Engineer for Voltrix, and later as a Sales Engineer for Corvane. After his MBA, he served as a Strategy Consultant for Ribeira Business School. Originally from Portugal, Marco enjoys designing and launching new ideas, international communities, mindfulness retreats, and musical improvisation. He nurtures a close connection to Willow Grove Mindfulness Centre, where he has practiced and volunteered over 9 months. He has a broad experience of sharing the benefits of mindfulness with others.</p>
  <p class="more-link">More about the facilitator: profiles.brightfoldjoy.io/marcovella</p>

  <div class="footer-rule"></div>
  <footer>
    <div class="contact contact-email">
      <svg width="9" height="9" viewBox="0 0 9 9" aria-hidden="true"><circle cx="4.5" cy="4.5" r="4.5" fill="#2a7fbf"/><rect x="2" y="3" width="5" height="3.2" fill="none" stroke="#fff" stroke-width="0.6"/><polyline points="2,3 4.5,5 7,3" fill="none" stroke="#fff" stroke-width="0.6"/></svg>
      <span>info@brightfoldjoy.io</span>
    </div>
    <div class="contact-divider"></div>
    <p class="contact-label">Information<br>&amp; Booking</p>
    <div class="contact contact-phone">
      <svg width="10" height="10" viewBox="0 0 10 10" aria-hidden="true"><circle cx="5" cy="5" r="5" fill="#2a7fbf"/><path d="M3.2 2.6c.3-.3.7-.3.9 0l.5.7c.2.3.1.6-.1.8l-.3.3c.3.7.8 1.2 1.5 1.5l.3-.3c.2-.2.5-.3.8-.1l.7.5c.3.2.3.6 0 .9l-.4.4c-1.9-.2-4-2.3-4.2-4.2z" fill="#fff"/></svg>
      <span>Tel: +34 611 482 395</span>
      <span class="dot-icon" style="background: var(--green);"></span>
    </div>
  </footer>

  <div class="colour-bar"><span></span><span></span><span></span></div>
</main>
</body>
</html>
```